Customizing and design a blog from the scratch

I need a blog designer to customize my blog from scratch, I have create the blog with Wordpress with Divi theme but I have nothing to do with the layout and the design, I can only provide the menu list I have in my mind and the skill of writing,I need a talented blog designer to help me with that.Thanks

Colors

Designer to choose colors to be used in the design.

Requirements
Nice to have
• My blog name is
• Greet every new dawn
• So I would like an inspiring background, the blog will be having 5 main pages
• 1. Education
• 2.Kids corner
• 3.Health and fitness
• 4.Beauty and fashion
• 5.Arabian corner
• UNDER each of them I will post a daily new post.
• I would like to have a home page which side will write a brief post a bout the page.
• Hope that helps!

```html
<!DOCTYPE html>
<html lang="en">
<head>
<meta charset="utf-8">
<title>Greet every new dawn</title>
<link href="https://fonts.googleapis.com/css2?family=Montserrat:wght@400;500;600;700&display=swap" rel="stylesheet">
<style>
:root{
  --yellow:#ffc40d;
  --yellow-dark:#efb500;
  --ink:#1f1f1f;
  --muted:#8a8a8a;
  --band:#e6e6e6;
  --card-light:#efefef;
  --white:#ffffff;
  --footer:#1b1b1b;
}
*{box-sizing:border-box;margin:0;padding:0}
html,body{width:1200px;height:4769px;overflow:hidden}
body{font-family:'Montserrat',sans-serif;color:var(--ink);background:var(--white)}
a{color:inherit;text-decoration:none}

/* hero */
.hero{position:relative;height:615px;overflow:hidden}
.hero-photo{position:absolute;inset:0;background:linear-gradient(100deg,#6a5544 0%,#a88a70 25%,#5d4a3c 50%,#2e2a27 75%,#4a4036 100%)}
.site-header{position:absolute;top:0;left:144px;right:144px;height:70px;display:flex;align-items:center;justify-content:space-between}
.site-name{color:var(--yellow);font-size:30px;font-weight:500}
.main-nav{display:flex;align-items:center;gap:0;font-size:12px;color:var(--white);text-transform:uppercase}
.main-nav a{margin-right:30px}
.main-nav .active{color:var(--yellow)}
.search{width:178px;border-bottom:1px solid #ddd;display:flex;justify-content:space-between;align-items:center;padding-bottom:4px;margin-left:14px;font-size:12px;text-transform:none}
.featured{position:absolute;left:768px;top:167px;width:288px;height:277px;background:rgba(25,25,25,.88);padding:22px 16px;text-align:right;color:var(--white)}
.featured h2{color:var(--yellow);font-size:31px;font-weight:500;margin-bottom:10px}
.featured .lead{font-size:15px;line-height:1.5}
.featured .date{color:var(--yellow);font-size:11px;margin:10px 0 12px}
.featured .blurb{font-size:9.5px;line-height:1.9;color:#bbb}
.btn{display:inline-block;background:var(--yellow);color:var(--ink);font-weight:700;font-size:12px;text-transform:uppercase;padding:11px 16px}
.featured .btn{margin-top:14px}
.slide-arrow{position:absolute;top:287px;width:40px;height:40px;border-radius:50%;display:flex;align-items:center;justify-content:center}
.slide-arrow.prev{left:50px;background:rgba(255,255,255,.35)}
.slide-arrow.next{left:1106px;background:var(--white)}

/* categories */
.education-wrap{height:891px;position:relative}
.category-bar{position:absolute;left:144px;top:-28px;width:912px;height:200px;background:var(--yellow);display:flex;border-bottom:3px solid #d9a300}
.category{flex:1;display:flex;flex-direction:column;align-items:center;padding-top:34px;text-align:center;font-weight:600;font-size:18px;text-transform:uppercase;line-height:1.3;border-right:1px solid rgba(0,0,0,.08);position:relative}
.category:last-child{border-right:0}
.category svg{width:72px;height:72px;margin-bottom:16px}
.category.current{background:var(--yellow-dark)}
.category.current::after{content:"";position:absolute;bottom:-22px;left:50%;margin-left:-18px;border:18px solid transparent;border-top:20px solid var(--yellow-dark);border-bottom:0}

/* article sections */
.topic{height:728px;padding-top:72px}
.topic.band{background:var(--band)}
.education-wrap .topic{height:auto;padding-top:253px}
.topic h2{text-align:center;font-size:31px;font-weight:500;line-height:40px;text-transform:uppercase}
.rule{width:120px;height:2px;background:#9a9a9a;margin:10px auto 0}
.grid{width:912px;height:456px;margin:22px auto 0;display:flex;justify-content:space-between}
.grid.reverse{flex-direction:row-reverse}
.lead-card,.list{width:440px}
.lead-card{background:var(--card-light);position:relative}
.band .lead-card,.band .item{background:var(--white)}
.lead-card .photo{height:256px}
.badge{position:absolute;left:0;top:0;width:63px;height:78px;background:#222;color:var(--white);text-align:center;padding-top:6px}
.badge b{display:block;font-size:32px;font-weight:500;line-height:34px}
.badge span{font-size:17px}
.lead-card .body{padding:20px 24px}
.lead-card h3{font-size:16px;font-weight:500;line-height:1.4}
.lead-card p{font-size:9.5px;line-height:2;color:#555;margin:10px 0 16px}
.list{display:flex;flex-direction:column;justify-content:space-between}
.item{height:144px;background:var(--card-light);display:flex}
.item .photo{width:160px;flex:none}
.item .text{padding:14px 18px}
.item h4{font-size:13px;font-weight:500;line-height:1.35}
.item .date{font-size:11px;color:var(--muted);margin:6px 0}
.item p{font-size:9.5px;line-height:1.9;color:#555}
.view-all{display:block;width:max-content;margin:28px auto 0;font-size:14px;text-decoration:underline;text-transform:uppercase}

/* newsletter */
.newsletter{height:260px;background:var(--band);padding-top:70px;text-align:center}
.newsletter h2{font-size:31px;font-weight:500;text-transform:uppercase}
.newsletter .rule{margin-top:10px}
.signup{display:flex;width:430px;margin:38px auto 0;height:38px}
.signup .field{flex:1;background:var(--white);border:1px solid #d0d0d0;text-align:left;padding:10px 14px;font-size:12px;color:#777}
.signup .btn{padding:12px 18px;font-size:12px}

/* footer */
.site-footer{height:93px;background:var(--footer);color:#aaa;font-size:10.5px;padding:22px 144px 0;position:relative}
.site-footer .links{margin-bottom:16px}
.socials{position:absolute;right:144px;top:28px;display:flex;gap:20px}
.socials span{width:18px;height:18px;border-radius:50%;background:#777;display:block}
</style>
</head>
<body>

<header class="hero">
  <div class="hero-photo" role="img" aria-label="Young woman in glasses smiling while typing on a laptop at a desk"></div>
  <div class="site-header">
    <div class="site-name">Greet every new dawn</div>
    <nav class="main-nav">
      <a class="active" href="#">Categories</a><a href="#">Bio</a><a href="#">Contact</a>
      <div class="search">Search
        <svg width="11" height="11" viewBox="0 0 12 12"><circle cx="5" cy="5" r="3.6" fill="none" stroke="#fff" stroke-width="1.6"/><line x1="7.7" y1="7.7" x2="11" y2="11" stroke="#fff" stroke-width="1.8"/></svg>
      </div>
    </nav>
  </div>
  <article class="featured">
    <h2>Featured Post</h2>
    <p class="lead">Vivamus efficitur ex condimen tum, malesuada eros eget</p>
    <p class="date">31 August, 2019</p>
    <p class="blurb">Sed tellus ex, imperdiet eget gravida sit amet, volutpat eget turpis. In nec ultricies est. Etiam mattis augue vehicula odio posuere.</p>
    <a class="btn" href="#">Read more</a>
  </article>
  <a class="slide-arrow prev" href="#"><svg width="14" height="14" viewBox="0 0 14 14"><path d="M9 2 4 7l5 5" fill="none" stroke="#222" stroke-width="2"/></svg></a>
  <a class="slide-arrow next" href="#"><svg width="14" height="14" viewBox="0 0 14 14"><path d="M5 2l5 5-5 5" fill="none" stroke="#222" stroke-width="2"/></svg></a>
</header>

<div class="education-wrap">
  <nav class="category-bar">
    <a class="category current" href="#">
      <svg viewBox="0 0 72 72" fill="none" stroke="#222" stroke-width="2.2"><path d="M8 18h22c4 0 6 2 6 6v36c0-3-2-5-6-5H8z"/><path d="M64 18H42c-4 0-6 2-6 6v36c0-3 2-5 6-5h22z"/><path d="M4 24v36h28M68 24v36H40"/><path d="M14 28h14M14 35h14M14 42h14M44 28h14M44 35h14M44 42h14"/></svg>
      Education</a>
    <a class="category" href="#">
      <svg viewBox="0 0 72 72" fill="none" stroke="#222" stroke-width="2.2"><circle cx="24" cy="28" r="11"/><circle cx="48" cy="28" r="11"/><path d="M12 28c0-10 6-16 12-16s12 6 12 16M36 28c0-10 6-16 12-16s12 6 12 16"/><path d="M8 64c0-12 7-20 16-20s16 8 16 20M32 64c0-12 7-20 16-20s16 8 16 20"/></svg>
      Kids corner</a>
    <a class="category" href="#">
      <svg viewBox="0 0 72 72" fill="none" stroke="#222" stroke-width="2.2"><path d="M24 48l24-24"/><rect x="40" y="8" width="10" height="24" rx="2" transform="rotate(45 45 20)"/><rect x="50" y="16" width="8" height="18" rx="2" transform="rotate(45 54 25)"/><rect x="22" y="40" width="10" height="24" rx="2" transform="rotate(45 27 52)"/><rect x="14" y="38" width="8" height="18" rx="2" transform="rotate(45 18 47)"/></svg>
      Health and<br>fitness</a>
    <a class="category" href="#">
      <svg viewBox="0 0 72 72" fill="none" stroke="#222" stroke-width="2.2"><path d="M22 36c-4-18 6-28 16-28s18 8 14 26"/><circle cx="36" cy="34" r="13"/><path d="M30 47v6M42 47v6M18 66c2-8 8-13 18-13s16 5 18 13"/></svg>
      Beauty and<br>fashion</a>
    <a class="category" href="#">
      <svg viewBox="0 0 72 72" fill="none" stroke="#222" stroke-width="2.2"><path d="M34 4v60M26 64V30l8-12M42 64V26"/><path d="M42 26c10 4 16 14 16 26H42"/><path d="M20 64h36M26 44h16"/></svg>
      Arabian<br>corner</a>
  </nav>

  <section class="topic">
    <h2>Education</h2><div class="rule"></div>
    <div class="grid">
      <article class="lead-card">
        <div class="photo" role="img" aria-label="Schoolchildren writing at their desks in a classroom" style="background:linear-gradient(135deg,#9a7b5a,#d8c3a4 55%,#7b6048)"></div>
        <div class="badge"><b>31</b><span>Aug</span></div>
        <div class="body">
          <h3>Vivamus lacus justo, ultrices nec erat in, euismod iaculis mauris.</h3>
          <p>Vivamus eleifend vitae nulla vel malesuada. In ac malesuada lacus, et consectetur ante. Fusce vitae lectus sit amet mi pulvinar maximus. Aenean placerat, nibh vel accumsan aliquet, magna nibh accumsan.</p>
          <a class="btn" href="#">Read more</a>
        </div>
      </article>
      <div class="list">
        <article class="item"><div class="photo" role="img" aria-label="Students working together around a classroom table" style="background:linear-gradient(135deg,#5b4a3d,#a99a88)"></div><div class="text"><h4>Vestibulum ante primis in faucibus orci luctus et ultrices posuere</h4><p class="date">31 August, 2019</p><p>Fusce vitae lectus sit amet mi pulvinar maximus. Aenean placerat, nibh vel accumsan aliquet, magna nibh accumsan.</p></div></article>
        <article class="item"><div class="photo" role="img" aria-label="Pupils writing in notebooks at colourful desks" style="background:linear-gradient(135deg,#c9b27a,#6d8fb4)"></div><div class="text"><h4>Phasellus nisl est, condimentum vitae faucibus in, sollicitudin vel metus</h4><p class="date">31 August, 2019</p><p>Fusce vitae lectus sit amet mi pulvinar maximus. Aenean placerat, nibh vel accumsan aliquet, magna nibh accumsan.</p></div></article>
        <article class="item"><div class="photo" role="img" aria-label="Classroom with students seated in rows facing a teacher" style="background:linear-gradient(135deg,#c8c4bd,#6b5a4c)"></div><div class="text"><h4>Curabitur ac elit leo. In eleifend dui tellus, in scelerisque elit porttitor</h4><p class="date">31 August, 2019</p><p>Fusce vitae lectus sit amet mi pulvinar maximus. Aenean placerat, nibh vel accumsan aliquet, magna nibh accumsan.</p></div></article>
      </div>
    </div>
    <a class="view-all" href="#">View all education articles</a>
  </section>
</div>

<section class="topic band">
  <h2>Kids corner</h2><div class="rule"></div>
  <div class="grid reverse">
    <article class="lead-card">
      <div class="photo" role="img" aria-label="Young boy in a grey shirt looking at the camera" style="background:linear-gradient(135deg,#5a4d44,#b7aea4 55%,#d9d3cc)"></div>
      <div class="badge"><b>31</b><span>Aug</span></div>
      <div class="body">
        <h3>Vivamus lacus justo, ultrices nec erat in, euismod iaculis mauris.</h3>
        <p>Vivamus eleifend vitae nulla vel malesuada. In ac malesuada lacus, et consectetur ante. Fusce vitae lectus sit amet mi pulvinar maximus. Aenean placerat, nibh vel accumsan aliquet, magna nibh accumsan.</p>
        <a class="btn" href="#">Read more</a>
      </div>
    </article>
    <div class="list">
      <article class="item"><div class="photo" role="img" aria-label="Mother holding and kissing her baby" style="background:linear-gradient(135deg,#f1e6dc,#c99e80)"></div><div class="text"><h4>Vestibulum ante primis in faucibus orci luctus et ultrices posuere</h4><p class="date">31 August, 2019</p><p>Fusce vitae lectus sit amet mi pulvinar maximus. Aenean placerat, nibh vel accumsan aliquet, magna nibh accumsan.</p></div></article>
      <article class="item"><div class="photo" role="img" aria-label="Child in a helmet playing among bamboo" style="background:linear-gradient(135deg,#6f8a3a,#c7c46a)"></div><div class="text"><h4>Phasellus nisl est, condimentum vitae faucibus in, sollicitudin vel metus</h4><p class="date">31 August, 2019</p><p>Fusce vitae lectus sit amet mi pulvinar maximus. Aenean placerat, nibh vel accumsan aliquet, magna nibh accumsan.</p></div></article>
      <article class="item"><div class="photo" role="img" aria-label="Two children with colourful building blocks" style="background:linear-gradient(135deg,#e34a3a,#f3c13a 50%,#3a7fd0)"></div><div class="text"><h4>Curabitur ac elit leo. In eleifend dui tellus, in scelerisque elit porttitor</h4><p class="date">31 August, 2019</p><p>Fusce vitae lectus sit amet mi pulvinar maximus. Aenean placerat, nibh vel accumsan aliquet, magna nibh accumsan.</p></div></article>
    </div>
  </div>
  <a class="view-all" href="#">View all kids corner articles</a>
</section>

<section class="topic">
  <h2>Health and fitness</h2><div class="rule"></div>
  <div class="grid">
    <article class="lead-card">
      <div class="photo" role="img" aria-label="Athlete doing dips on outdoor parallel bars" style="background:linear-gradient(135deg,#8fb2c9,#d9d2c2 50%,#6a5648)"></div>
      <div class="badge"><b>31</b><span>Aug</span></div>
      <div class="body">
        <h3>Vivamus lacus justo, ultrices nec erat in, euismod iaculis mauris.</h3>
        <p>Vivamus eleifend vitae nulla vel malesuada. In ac malesuada lacus, et consectetur ante. Fusce vitae lectus sit amet mi pulvinar maximus. Aenean placerat, nibh vel accumsan aliquet, magna nibh accumsan.</p>
        <a class="btn" href="#">Read more</a>
      </div>
    </article>
    <div class="list">
      <article class="item"><div class="photo" role="img" aria-label="Trainer guiding a woman through floor exercises" style="background:linear-gradient(135deg,#e4e0da,#5b544e)"></div><div class="text"><h4>Vestibulum ante primis in faucibus orci luctus et ultrices posuere</h4><p class="date">31 August, 2019</p><p>Fusce vitae lectus sit amet mi pulvinar maximus. Aenean placerat, nibh vel accumsan aliquet, magna nibh accumsan.</p></div></article>
      <article class="item"><div class="photo" role="img" aria-label="Group fitness class doing squats in a studio" style="background:linear-gradient(135deg,#7a5a44,#c7a68a)"></div><div class="text"><h4>Phasellus nisl est, condimentum vitae faucibus in, sollicitudin vel metus</h4><p class="date">31 August, 2019</p><p>Fusce vitae lectus sit amet mi pulvinar maximus. Aenean placerat, nibh vel accumsan aliquet, magna nibh accumsan.</p></div></article>
      <article class="item"><div class="photo" role="img" aria-label="Woman holding a yoga pose outdoors among trees" style="background:linear-gradient(135deg,#2f4a2a,#8fae6a)"></div><div class="text"><h4>Curabitur ac elit leo. In eleifend dui tellus, in scelerisque elit porttitor</h4><p class="date">31 August, 2019</p><p>Fusce vitae lectus sit amet mi pulvinar maximus. Aenean placerat, nibh vel accumsan aliquet, magna nibh accumsan.</p></div></article>
    </div>
  </div>
  <a class="view-all" href="#">View all health and fitness articles</a>
</section>

<section class="topic band">
  <h2>Beauty and fashion</h2><div class="rule"></div>
  <div class="grid reverse">
    <article class="lead-card">
      <div class="photo" role="img" aria-label="Hairdresser styling a client's hair in a salon" style="background:linear-gradient(135deg,#3c3834,#a49a8e 55%,#e0d6c6)"></div>
      <div class="badge"><b>31</b><span>Aug</span></div>
      <div class="body">
        <h3>Vivamus lacus justo, ultrices nec erat in, euismod iaculis mauris.</h3>
        <p>Vivamus eleifend vitae nulla vel malesuada. In ac malesuada lacus, et consectetur ante. Fusce vitae lectus sit amet mi pulvinar maximus. Aenean placerat, nibh vel accumsan aliquet, magna nibh accumsan.</p>
        <a class="btn" href="#">Read more</a>
      </div>
    </article>
    <div class="list">
      <article class="item"><div class="photo" role="img" aria-label="Makeup artist applying eye makeup to a model" style="background:linear-gradient(135deg,#6b4b3a,#d8b49a)"></div><div class="text"><h4>Vestibulum ante primis in faucibus orci luctus et ultrices posuere</h4><p class="date">31 August, 2019</p><p>Fusce vitae lectus sit amet mi pulvinar maximus. Aenean placerat, nibh vel accumsan aliquet, magna nibh accumsan.</p></div></article>
      <article class="item"><div class="photo" role="img" aria-label="Little girl in a pink outfit posing" style="background:linear-gradient(135deg,#f1e4da,#d9507a)"></div><div class="text"><h4>Phasellus nisl est, condimentum vitae faucibus in, sollicitudin vel metus</h4><p class="date">31 August, 2019</p><p>Fusce vitae lectus sit amet mi pulvinar maximus. Aenean placerat, nibh vel accumsan aliquet, magna nibh accumsan.</p></div></article>
      <article class="item"><div class="photo" role="img" aria-label="Girl in a tutu applying makeup at a mirror" style="background:linear-gradient(135deg,#e9e1d8,#e7a9b4)"></div><div class="text"><h4>Curabitur ac elit leo. In eleifend dui tellus, in scelerisque elit porttitor</h4><p class="date">31 August, 2019</p><p>Fusce vitae lectus sit amet mi pulvinar maximus. Aenean placerat, nibh vel accumsan aliquet, magna nibh accumsan.</p></div></article>
    </div>
  </div>
  <a class="view-all" href="#">View all beauty and fashion articles</a>
</section>

<section class="topic">
  <h2>Arabian corner</h2><div class="rule"></div>
  <div class="grid">
    <article class="lead-card">
      <div class="photo" role="img" aria-label="City skyline with tall towers under a blue sky" style="background:linear-gradient(180deg,#7fb0d8,#b9c6cf 55%,#a48d74)"></div>
      <div class="badge"><b>31</b><span>Aug</span></div>
      <div class="body">
        <h3>Vivamus lacus justo, ultrices nec erat in, euismod iaculis mauris.</h3>
        <p>Vivamus eleifend vitae nulla vel malesuada. In ac malesuada lacus, et consectetur ante. Fusce vitae lectus sit amet mi pulvinar maximus. Aenean placerat, nibh vel accumsan aliquet, magna nibh accumsan.</p>
        <a class="btn" href="#">Read more</a>
      </div>
    </article>
    <div class="list">
      <article class="item"><div class="photo" role="img" aria-label="Two women in headscarves smiling together" style="background:linear-gradient(135deg,#2a2522,#8f7a6a)"></div><div class="text"><h4>Vestibulum ante primis in faucibus orci luctus et ultrices posuere</h4><p class="date">31 August, 2019</p><p>Fusce vitae lectus sit amet mi pulvinar maximus. Aenean placerat, nibh vel accumsan aliquet, magna nibh accumsan.</p></div></article>
      <article class="item"><div class="photo" role="img" aria-label="Camel against a desert sky" style="background:linear-gradient(180deg,#3e6fb0,#c89456)"></div><div class="text"><h4>Phasellus nisl est, condimentum vitae faucibus in, sollicitudin vel metus</h4><p class="date">31 August, 2019</p><p>Fusce vitae lectus sit amet mi pulvinar maximus. Aenean placerat, nibh vel accumsan aliquet, magna nibh accumsan.</p></div></article>
      <article class="item"><div class="photo" role="img" aria-label="Narrow old town street with traditional buildings" style="background:linear-gradient(180deg,#6fa4d8,#b89a78)"></div><div class="text"><h4>Curabitur ac elit leo. In eleifend dui tellus, in scelerisque elit porttitor</h4><p class="date">31 August, 2019</p><p>Fusce vitae lectus sit amet mi pulvinar maximus. Aenean placerat, nibh vel accumsan aliquet, magna nibh accumsan.</p></div></article>
    </div>
  </div>
  <a class="view-all" href="#">View all arabian corner articles</a>
</section>

<section class="newsletter">
  <h2>Newsletter sign up</h2><div class="rule"></div>
  <form class="signup"><div class="field">Email Address</div><a class="btn" href="#">Subscribe</a></form>
</section>

<footer class="site-footer">
  <p class="links">Home &nbsp;|&nbsp; Categories &nbsp;|&nbsp; Bio &nbsp;|&nbsp; Contact</p>
  <p>Copyright © 2019 &nbsp;Greet every new dawn. &nbsp;All rights reserved.</p>
  <div class="socials"><span></span><span></span><span></span><span></span><span></span></div>
</footer>

</body>
</html>
```